Wordpress Theme for Medical Clinics

** Please view updated Sitemap2.pdf doc to clarify some confusion ***

This is a multiuser WordPress subscription site for medical clinics. Please see attachment for sitemap. Please do not include extra content like social media icons, search bars, or images. If you have questions, please ask for clarification.
The site contains the following pages and sub-pages:

1. Home
2. Our Clinic
2a. Our Clinic > Mission
2b. Our Clinic > Services
2c. Our Clinic > Clinic Policies
2d. Our Clinic > Schedules
3. Our Staff
3a. Our Staff > [Staff member page]
4. Resources
4a. Resources > Patient Health (index)
4b. Resources > Patient Health (index) > [post]
4c. Resources > Links
4d. Resources > Forms
5. Alerts
5a. Alerts > [Alert Page]
6. Contact Us

Includes the Following Pages, Subpages, and Content
1. Home
a. About Us
b. Our Staff
c. Bulletins
d. Accepting New Patients (shown as an alert widget)
e. Links
i. Physician Toolbox
ii. Book an Appointment
f. Clinic Policies
i. Show first 3 policies (e.g. Late Arrivals, Missed Appointments, Fees)
ii. Link to Clinic Policies page
g. Primary widget (displayed on all pages)
i. Hours of operation
ii. Contact Info
1. Tel
2. Fax
3. Email
4. Address
5. Get directions (link to Google Maps)
2. Our Clinic
a. Main Page
i. Clinic Name
ii. Overview
iii. Languages Spoken
iv. Secondary Navigation
1. Mission
2. Services
3. Clinic Policies
4. Schedules (see attachment)
b. Our Clinic > Mission
c. Our Clinic > Services
i. For each service include service TITLE and DESCRIPTION
d. Our Clinic > Clinic Policies
i. For each policy include policy TITLE and DESCRIPTION
ii. Include the following policies in mockup
1. Late arrivals
2. Missed appointments
3. Fees for missed appointments
4. Referrals and follow-ups
5. Services not covered by RDV
6. Information for TQL patients
7. Medical Legal Reports
e. Our Clinic > Schedules
3. Our Staff
a. Main Page
i. Display a list of staff members. Include NAME and DESIGNATION
b. Our Staff > [Staff Name]
i. Include NAME, PICTURE, DESIGNATION, and BIO
4. Resources
a. Resources > Patient Health
i. Main Page
1. Posts (ordered by date)
a. Title
b. Summary
2. Side Navigation
a. Post Categories
ii. Patient Health > [post title]
1. Title
2. Post Category
3. Date
4. Author
5. Summary
6. Body
b. Resources > Links
1. Secondary Navigation - Categories
a. Sample Categories:
i. Local Services
ii. RDV and Drug Coverage
iii. Mental Health Resources
2. Category page
a. Include the following links in the 'Local Services' category
i. Hypertension clinics
ii. Home Care services
iii. Vaccine Clinics
c. Resources > Forms
i. Display a table with form TITLE and CATEGORY
ii. Side Navigation
1. Form Categories
a. Use the following sample Categories
i. Referrals
ii. Insurance
iii. Intake
iv. Discharge
v. Waivers
5. Alerts
a. Main page
i. List of all Alert posts
1. Include post TITLE as a link to the post
ii. Side Navigation
1. Alerts Archive
a. shown as Month + Number of posts
iii. Alerts > [Alert page]
1. Include TITLE, DATE, AUTHOR, BODY
6. Contact Us
a. Map
b. Hours of operation
c. Address
d. Phone number
e. Fax number
e. Fax number
f. Map
g. Email

Design notes:
- fixed width
- responsive (need designs for mobile, tablet, and desktop)
- simple, dark font, white background
- use Font Awesome icons where needed
- user adds own logo

Target Market(s)

Medical Clinics

Industry/Entity Type

Medical

Number of Pages Required

5+ page

Font styles to use
Serif
Sans Serif

Requirements
Must have
• Please keep designs very simple.
• Examples:
• https://www.quandrix.com/install
• http://www.tervolane.com/company/about-us
• http://brightnumberhub.org/
• http://www.vorn.com/
Should not have
• Minimal or no use of shadows and gradients

```html
<!DOCTYPE html>
<html lang="en">
<head>
<meta charset="utf-8">
<title>Clinic Name – Home</title>
<link href="https://fonts.googleapis.com/css2?family=Dosis:wght@400;500;600;700&family=Open+Sans:wght@400;600&display=swap" rel="stylesheet">
<style>
:root{
  --blue:#2f95f0;
  --blue-dark:#1f7fd6;
  --ink:#222;
  --text:#6b6b6b;
  --muted:#9a9a9a;
  --rule:#e2e2e2;
  --band:#f4f4f4;
  --band-2:#ececec;
  --navy:#3c4e6e;
  --navy-text:#c9d2e2;
  --white:#fff;
}
*{box-sizing:border-box;margin:0;padding:0}
html,body{width:1200px;height:3172px;overflow:hidden;background:var(--white)}
body{font-family:"Open Sans",Arial,sans-serif;color:var(--text);position:relative;font-size:14px}
.abs{position:absolute}
h1,h2,h3,h4,.display{font-family:"Dosis",Arial,sans-serif;font-weight:500}
.btn{display:flex;align-items:center;justify-content:center;background:var(--blue);color:var(--white);border-radius:5px;font-family:"Dosis",Arial,sans-serif;font-size:19px}

/* hero */
.hero{left:0;top:0;width:1200px;height:732px;background:linear-gradient(100deg,#dfe9f1 0%,#f4f6f8 35%,#e8eef3 60%,#d7e2ec 100%)}
.hero-photo{left:0;top:0;width:1200px;height:732px;background:radial-gradient(ellipse at 30% 45%,rgba(180,195,210,.55),transparent 60%),radial-gradient(ellipse at 80% 40%,rgba(170,188,205,.5),transparent 55%)}
.nav{left:0;top:50px;width:1200px;height:40px;font-size:16px;font-family:"Dosis",Arial,sans-serif;color:var(--ink)}
.nav a{position:absolute;top:8px;text-decoration:none;color:var(--ink);font-weight:500}
.nav a.current{color:var(--blue)}
.brand{left:502px;top:0;font-size:30px;color:var(--blue);font-weight:600;font-family:"Dosis",Arial,sans-serif}
.nav .btn{left:846px;top:2px;width:142px;height:36px;font-size:17px}
.hero h1{left:262px;top:398px;font-size:64px;color:var(--blue);font-weight:600;line-height:1}
.hero .sub{left:262px;top:466px;font-size:40px;color:#1d4f8c;font-weight:600;line-height:1}
.hero p{left:264px;top:512px;width:420px;font-size:15px;line-height:22px;color:#333}
.hero .btn{left:262px;top:603px;width:206px;height:40px}

/* clinic */
.section-title{font-size:27px;color:var(--blue)}
.clinic-title{left:180px;top:770px}
.clinic-text{left:180px;top:814px;width:570px;font-size:12.5px;line-height:18px;color:var(--muted)}
.clinic-photo{left:180px;top:899px;width:570px;height:193px;background:linear-gradient(90deg,#e9eef3,#f3f5f7 45%,#dde6ee);border:1px solid var(--rule)}
.hours{left:774px;top:772px;width:314px;height:322px;border:2px solid var(--rule)}
.hours h3{position:absolute;left:20px;top:12px;font-size:27px;color:var(--blue);font-weight:500}
.hours table{position:absolute;left:20px;top:62px;width:274px;border-collapse:collapse;font-size:13px}
.hours td{height:24.5px;border-bottom:1px solid var(--rule);color:var(--ink)}
.hours td.t{color:var(--blue);text-align:right}
.hours .btn{left:20px;top:260px;width:274px;height:46px;font-size:20px}

/* services */
.services{left:0;top:1145px;width:1200px;height:533px;background:var(--band)}
.services h2{left:0;top:1178px;width:1200px;text-align:center;font-size:29px;color:var(--blue)}
.services-lead{left:400px;top:1222px;width:400px;text-align:center;font-size:12.5px;line-height:17px;color:var(--muted)}
.col-head{font-size:30px;color:var(--ink);display:flex;align-items:center;gap:8px}
.col-text{font-size:12.5px;line-height:17px;color:var(--muted)}
.staff-head{left:180px;top:1304px}
.staff-text{left:180px;top:1352px;width:270px}
.staff-list{left:180px;top:1418px;width:272px;display:grid;grid-template-columns:1fr 1fr;column-gap:16px;row-gap:0;font-size:11px;color:var(--ink)}
.staff-list span{border-bottom:1px solid var(--rule);padding:8px 0}
.small-btn{height:26px;font-size:13px;border-radius:4px}
.staff-btn{left:180px;top:1541px;width:95px}
.mascot{left:476px;top:1322px;width:238px;height:318px;background:radial-gradient(ellipse at 50% 45%,#dfe9f3 0%,#eef3f8 55%,transparent 72%)}
.links-head{left:785px;top:1304px}
.links-text{left:785px;top:1352px;width:270px}
.links-list{left:785px;top:1418px;width:270px;display:grid;grid-template-columns:1fr 1fr;row-gap:10px;font-size:11px;color:var(--ink)}
.links-list span{display:flex;align-items:center;gap:6px}
.new-patients{left:785px;top:1528px;width:265px;height:100px;background:var(--blue);border-radius:8px;color:var(--white)}
.new-patients h4{position:absolute;left:48px;top:12px;font-size:21px;color:var(--white)}
.new-patients p{position:absolute;left:14px;top:60px;font-size:11px}
.new-patients .dark{position:absolute;left:153px;top:52px;width:100px;height:32px;background:#2a3547;color:var(--white);border-radius:4px;font-size:12px;display:flex;align-items:center;justify-content:center}

/* alerts + policies */
.lower{left:0;top:1678px;width:1200px;height:365px;background:var(--band-2)}
.panel{background:var(--white);border:1px solid #dedede}
.panel-head{height:62px;background:var(--blue);color:var(--white);font-family:"Dosis",Arial,sans-serif;font-size:27px;display:flex;align-items:center;justify-content:space-between;padding:0 20px}
.alerts{left:143px;top:1692px;width:549px;height:322px}
.alert-row{display:flex;justify-content:space-between;align-items:center;height:64px;margin:0 20px;border-bottom:1px solid var(--rule);font-family:"Dosis",Arial,sans-serif;font-size:17px;color:var(--blue-dark)}
.alert-row.open{height:40px;border:none;margin-top:4px}
.alert-row b{font-size:30px;font-weight:400;color:var(--blue)}
.alert-body{margin:0 20px;font-size:12.5px;line-height:17px;color:var(--muted)}
.policies{left:737px;top:1692px;width:313px;height:322px}
.policies ol{list-style:none;padding:10px 18px 0}
.policies li{font-size:13px;color:var(--ink);height:27px;display:flex;align-items:center;border-bottom:1px solid #f0f0f0}
.policies li em{font-style:normal;color:var(--blue);width:32px}
.policies .small-btn{left:18px;top:280px;width:95px;position:absolute}

/* footer */
.footer{left:0;top:2043px;width:1200px;height:325px;background:var(--navy);color:var(--navy-text)}
.footer h4{font-size:19px;color:var(--white);font-weight:500;padding-bottom:8px;border-bottom:1px solid rgba(255,255,255,.15);margin-bottom:10px}
.fcol{position:absolute;top:60px;font-size:12.5px;line-height:26px}
.fcol p{line-height:17px}
.fhours div{display:flex;justify-content:space-between;width:230px;font-size:11px;line-height:24px}

/* contact */
.contact h2{left:0;top:2384px;width:1200px;text-align:center;font-size:36px;color:var(--ink);font-weight:600}
.contact .tag{left:0;top:2430px;width:1200px;text-align:center;font-size:10px;color:var(--muted)}
.contact .lead{left:330px;top:2472px;width:540px;text-align:center;font-size:14px;line-height:20px;color:var(--muted)}
.cinfo{top:2598px;width:260px;text-align:center}
.cinfo h4{font-size:17px;color:var(--ink);font-weight:600;font-family:"Open Sans",Arial,sans-serif}
.cinfo p{margin-top:24px;font-size:14px;color:var(--blue)}
.cinfo p.gray{color:var(--muted);line-height:18px}

/* map + form */
.map{left:0;top:2730px;width:1200px;height:442px;background:linear-gradient(135deg,#e6e6e6,#f1f1f1 40%,#e3e3e3 70%,#eeeeee)}
.form{left:180px;top:2749px;width:327px;height:383px;background:var(--white);border:1px solid #ddd;padding:22px 28px}
.form h3{font-size:17px;color:var(--ink);font-family:"Open Sans",Arial,sans-serif;font-weight:600}
.form p{font-size:10px;line-height:14px;color:var(--muted);margin-top:6px}
.field{height:36px;border:1px solid var(--rule);margin-top:14px;font-size:12px;color:var(--muted);padding:0 10px;display:flex;align-items:center}
.form .first{margin-top:46px}
.form .btn{position:absolute;right:28px;bottom:22px;width:118px;height:32px;font-size:14px;border-radius:2px}
.copyright{right:20px;top:3145px;font-size:11px;color:var(--muted)}
</style>
</head>
<body>

<header class="abs hero">
  <div class="abs hero-photo" role="img" aria-label="Photo of a team of doctors at a bright meeting table"></div>
  <nav class="abs nav">
    <a class="current" style="left:278px">Home</a>
    <a style="left:344px">Our Clinic</a>
    <a style="left:436px">Staff</a>
    <span class="abs brand">Clinic Name</span>
    <a style="left:671px">Resources</a>
    <a style="left:769px">Alerts</a>
    <span class="abs btn">Contact us</span>
  </nav>
  <h1 class="abs">Quality Care</h1>
  <div class="abs sub display">Provider For everyone!</div>
  <p class="abs">Highly skilled and Experienced medical staff comfortable and cozy patient rooms, latest diagnostic equipment.</p>
  <span class="abs btn">Book an Appointment</span>
</header>

<section>
  <h2 class="abs section-title clinic-title">Our Clinic</h2>
  <p class="abs clinic-text">Lorem ipsum dolor sit amet, consectetuer adipiscing elit, sed diam nonummy nibh euismod tincidunt ut laoreet dolore magna aliquam erat volutpat. Ut wisi enim ad minim veniam, quis nostrud exerci tation ullamcorper suscipit lobortis nisl ut aliquip ex ea commodo consequat.</p>
  <div class="abs clinic-photo" role="img" aria-label="Photo of smiling clinic staff standing together"></div>
  <aside class="abs hours">
    <h3>Hours of operation</h3>
    <table>
      <tr><td>Monday</td><td class="t">8:00 AM</td><td class="t">8:00 PM</td></tr>
      <tr><td>Tuesday</td><td class="t">8:00 AM</td><td class="t">8:00 PM</td></tr>
      <tr><td>Wednesday</td><td class="t">8:00 AM</td><td class="t">8:00 PM</td></tr>
      <tr><td>Thursday</td><td class="t">8:00 AM</td><td class="t">8:00 PM</td></tr>
      <tr><td>Friday</td><td class="t">8:00 AM</td><td class="t">8:00 PM</td></tr>
      <tr><td>Saturday</td><td class="t">8:00 AM</td><td class="t">8:00 PM</td></tr>
      <tr><td>Sunday</td><td class="t">8:00 AM</td><td class="t">8:00 PM</td></tr>
    </table>
    <span class="abs btn">Book an Appointment</span>
  </aside>
</section>

<section class="abs services"></section>
<h2 class="abs services-title" style="left:0;top:1178px;width:1200px;text-align:center;font-size:29px;color:var(--blue);font-family:'Dosis',Arial,sans-serif;font-weight:500">OUR SERVICES</h2>
<p class="abs services-lead">Lorem ipsum dolor sit amet, consectetuer adipiscing elit, sed diam nonummy nibh euismod tincidunt ut laoreet dolore magna aliquam erat</p>

<h3 class="abs col-head staff-head">
  <svg width="34" height="26" viewBox="0 0 34 26"><circle cx="17" cy="7" r="6" fill="#2f95f0"/><path d="M6 26a11 10 0 0 1 22 0z" fill="#2f95f0"/><circle cx="6" cy="10" r="4" fill="#2f95f0"/><circle cx="28" cy="10" r="4" fill="#2f95f0"/><path d="M0 24a6 7 0 0 1 9-6M34 24a6 7 0 0 0-9-6" fill="#2f95f0"/></svg>Staff</h3>
<p class="abs col-text staff-text">consectetuer adipiscing elit, sed diam nonummy nibh euismod tincidunt ut laoreet</p>
<div class="abs staff-list">
  <span>Dr. Alan Reyes, MD</span><span>Dr. Alan Reyes, MD</span>
  <span>Dr. Alan Reyes, MD</span><span>Dr. Alan Reyes, MD</span>
  <span>Dr. Alan Reyes, MD</span><span>Dr. Alan Reyes, MD</span>
</div>
<span class="abs btn small-btn staff-btn">View All</span>

<div class="abs mascot" role="img" aria-label="Illustration of a cartoon doctor holding a clipboard"></div>

<h3 class="abs col-head links-head">
  <svg width="26" height="26" viewBox="0 0 26 26" fill="none" stroke="#2f95f0" stroke-width="4" stroke-linecap="round"><path d="M11 15l-4 4a4 4 0 0 1-6-6l4-4a4 4 0 0 1 6 0"/><path d="M15 11l4-4a4 4 0 0 1 6 6l-4 4a4 4 0 0 1-6 0"/><path d="M9 17l8-8"/></svg>Links</h3>
<p class="abs col-text links-text">consectetuer adipiscing elit, sed diam nonummy nibh euismod tincidunt ut laoreet</p>
<div class="abs links-list">
  <span><svg width="12" height="10"><path d="M1 5l3 3 7-7" stroke="#2f95f0" stroke-width="2" fill="none"/></svg>TQL Clinics</span>
  <span><svg width="12" height="10"><path d="M1 5l3 3 7-7" stroke="#2f95f0" stroke-width="2" fill="none"/></svg>TQL Clinics</span>
  <span><svg width="12" height="10"><path d="M1 5l3 3 7-7" stroke="#2f95f0" stroke-width="2" fill="none"/></svg>TQL Clinics</span>
  <span><svg width="12" height="10"><path d="M1 5l3 3 7-7" stroke="#2f95f0" stroke-width="2" fill="none"/></svg>TQL Clinics</span>
  <span><svg width="12" height="10"><path d="M1 5l3 3 7-7" stroke="#2f95f0" stroke-width="2" fill="none"/></svg>TQL Clinics</span>
  <span><svg width="12" height="10"><path d="M1 5l3 3 7-7" stroke="#2f95f0" stroke-width="2" fill="none"/></svg>TQL Clinics</span>
</div>
<div class="abs new-patients">
  <svg class="abs" style="left:14px;top:14px" width="26" height="26" viewBox="0 0 26 26" fill="none" stroke="#fff" stroke-width="2"><circle cx="11" cy="8" r="5"/><path d="M2 24a9 8 0 0 1 18 0"/><path d="M21 8v8M17 12h8"/></svg>
  <h4>New Patients</h4>
  <p>Accepting new patients</p>
  <span class="dark">Contact us</span>
</div>

<section class="abs lower"></section>
<div class="abs panel alerts">
  <div class="panel-head">Alerts
    <svg width="34" height="30" viewBox="0 0 34 30"><path d="M17 1L33 29H1z" fill="#fff"/><rect x="15.5" y="10" width="3" height="11" fill="#2f95f0"/><rect x="15.5" y="23" width="3" height="3" fill="#2f95f0"/></svg>
  </div>
  <div class="alert-row">Alert Headline 1 <b>+</b></div>
  <div class="alert-row">Alert Headline 2 <b>+</b></div>
  <div class="alert-row open">Alert Headline 3 <b>–</b></div>
  <p class="alert-body">Ut wisi enim ad minim veniam, quis nostrud exerci tation ullamcorper suscipit lobortis nisl ut aliquip ex ea commodo consequat. Ut wisi enim ad minim veniam, quis nostrud exerci tation ullamcorper suscipit lobortis nisl ut aliquip ex ea commodo consequat.</p>
</div>
<div class="abs panel policies">
  <div class="panel-head">Clinic Policies
    <svg width="28" height="32" viewBox="0 0 28 32" fill="none" stroke="#fff" stroke-width="2.5"><path d="M4 2h14l6 6v22H4z"/><path d="M9 13h10M9 18h10M9 23h7"/></svg>
  </div>
  <ol>
    <li><em>01 .</em>Late arrivals</li>
    <li><em>02 .</em>Missed appointments</li>
    <li><em>03 .</em>Fees for missed appointments</li>
    <li><em>04 .</em>Referrals and follow-ups</li>
    <li><em>05 .</em>Services not covered by RDV</li>
    <li><em>06 .</em>Information for TQL patients</li>
    <li><em>07 .</em>Medical Legal Reports</li>
  </ol>
  <span class="btn small-btn">View All</span>
</div>

<footer class="abs footer">
  <div class="fcol" style="left:156px;width:170px">
    <h4>About</h4>
    <p>Ut wisi enim ad minim veniam, quis nostrud exerci tation ullamcorper suscipit lobortis nisl ut aliquip ex ea commodo consequat.</p>
  </div>
  <div class="fcol" style="left:423px;width:120px">
    <h4>Our Clinic</h4>
    <div>Mission</div><div>Services</div><div>Schedules</div><div>Policies</div>
  </div>
  <div class="fcol" style="left:610px;width:130px">
    <h4>Resources</h4>
    <div>Our clinic</div><div>Mission</div><div>Services</div>
  </div>
  <div class="fcol fhours" style="left:795px;width:230px">
    <h4>Hours of operation</h4>
    <div><span>Monday</span><span>8:00 AM – 8:00 PM</span></div>
    <div><span>Tuesday</span><span>8:00 AM – 8:00 PM</span></div>
    <div><span>Wednesday</span><span>8:00 AM – 8:00 PM</span></div>
    <div><span>Thursday</span><span>8:00 AM – 8:00 PM</span></div>
    <div><span>Friday</span><span>8:00 AM – 8:00 PM</span></div>
    <div><span>Saturday</span><span>8:00 AM – 8:00 PM</span></div>
  </div>
</footer>

<section class="contact">
  <h2 class="abs">CONTACT US NOW</h2>
  <div class="abs tag">We are here to help you today</div>
  <p class="abs lead">Ut wisi enim ad minim veniam, quis nostrud exerci tation ullamcorper suscipit lobortis nisl ut aliquip ex ea commodo consequat. Ut wisi enim ad minim veniam.</p>
  <div class="abs cinfo" style="left:66px"><h4>Phone Number</h4><p>123-555-0190</p></div>
  <div class="abs cinfo" style="left:455px"><h4>Clinic Address</h4><p class="gray">48 Alder Lane,<br>Fernvale</p></div>
  <div class="abs cinfo" style="left:782px"><h4>Email Address</h4><p>desk@fernvaleclinic.org</p></div>
</section>

<div class="abs map" role="img" aria-label="Street map showing the clinic location"></div>
<form class="abs form">
  <h3>Appointment Form</h3>
  <p>Ut wisi enim ad minim veniam, quis nostrud exerci tation ullamcorper suscipit lobortis nisl ut aliquip ex ea commodo consequat. Ut wisi enim ad minim veniam.</p>
  <div class="field first">Name</div>
  <div class="field">Email</div>
  <div class="field">Phone</div>
  <span class="btn">SEND</span>
</form>
<div class="abs copyright">© 2015 Copyright fernvaleclinic.org</div>

</body>
</html>
```